ICT Company specialising in web based information system design and implementation

We need a design for a new company in Australia called "Kestrel Hub". We design and develop customised web based information systems to automate business processes. This design needs to be based around Bootstrap from Plovane (http://plovane.codevault.example/)

Industry/Entity Type

Business

Requirements
Must have
• based on bootstrap plovane, site will be hosted on conrete5 platform. (http://plovane.codevault.example/)

```html
<!DOCTYPE html>
<html lang="en">
<head>
<meta charset="utf-8">
<title>Kestrel Hub</title>
<link rel="stylesheet" href="https://fonts.googleapis.com/css2?family=Gelasio:wght@400;700&family=Arimo:wght@400;700&display=swap">
<style>
:root{
  --lime:#9be22f;
  --lime-dark:#7fc11d;
  --sky:#3a9ad2;
  --sky-dark:#2f86bb;
  --paper:#dde3e5;
  --ink:#4a4a4a;
  --ink-soft:#555;
  --white:#fff;
  --red:#c4140f;
  --olive-top:#b4c93a;
  --olive-bottom:#7d9318;
  --steel-top:#9a9a9a;
  --steel-bottom:#6b6b6b;
  --rule:#a9b1b4;
  --frame:#b7e53c;
  --arrow:#1f78ab;
}
*{box-sizing:border-box;margin:0;padding:0}
html,body{width:980px;height:1200px;overflow:hidden}
body{position:relative;background:var(--paper);font-family:"Gelasio",Georgia,serif;color:var(--ink)}
.site-header{position:absolute;left:0;top:0;width:980px;height:92px;background:var(--lime);border-bottom:2px solid var(--lime-dark)}
.brand{position:absolute;left:132px;top:28px;display:flex;align-items:center;gap:10px}
.brand-mark{width:34px;height:34px;border-radius:50%;background:var(--red)}
.brand-name{font-family:"Gelasio",Georgia,serif;font-weight:700;font-size:24px;color:#1d3f8f}
.main-nav{position:absolute;left:488px;top:33px;display:flex;align-items:center;gap:22px;font-family:"Arimo",Arial,sans-serif;font-size:12px;font-weight:700;color:var(--white);text-transform:uppercase}
.main-nav a{color:var(--white);text-decoration:none}
.main-nav .is-active{background:var(--red);border-radius:15px;padding:7px 11px;box-shadow:inset 0 0 0 1px #8e0d08}
.hero{position:absolute;left:0;top:94px;width:980px;height:296px;background:var(--sky);border-bottom:1px solid var(--sky-dark)}
.hero-lead{position:absolute;left:90px;top:26px;width:800px;text-align:center;font-weight:700;font-size:14.5px;line-height:27px;color:var(--white);white-space:nowrap;text-shadow:0 1px 2px rgba(0,0,0,.35)}
.thumb{position:absolute;top:123px;width:158px;height:120px;border:2px solid var(--frame);background:linear-gradient(135deg,#36b8d8 0%,#5fb2c8 35%,#e0228f 60%,#f4e21a 80%,#9bd43a 100%)}
.slider-arrow{position:absolute;top:167px;width:34px;height:34px}
.ribbon{position:absolute;left:50%;transform:translateX(-50%);height:42px;display:flex;align-items:center;justify-content:center;font-weight:700;color:var(--white);text-shadow:0 1px 2px rgba(0,0,0,.4);clip-path:polygon(0 0,100% 0,94% 50%,100% 100%,0 100%,6% 50%)}
.ribbon--live{top:370px;width:272px;background:linear-gradient(var(--olive-top),var(--olive-bottom));font-size:20px;letter-spacing:1px}
.ribbon--blog{top:712px;width:270px;background:linear-gradient(var(--steel-top),var(--steel-bottom));font-size:20px}
.features{position:absolute;left:126px;top:455px;width:720px;display:flex}
.feature{width:240px;padding:0 10px;text-align:center}
.feature + .feature{border-left:1px solid #c3cacc}
.feature-title{display:flex;align-items:center;justify-content:center;gap:10px;font-size:19px;font-weight:700;color:#555;margin-bottom:14px;height:30px}
.feature-title svg{width:28px;height:28px}
.feature p{font-size:10.5px;line-height:18px;color:var(--ink-soft);height:150px}
.blog-rule{position:absolute;left:0;top:732px;width:980px;height:1px;background:var(--rule)}
.post{position:absolute;top:784px;width:330px;text-align:center}
.post h2{font-weight:400;font-size:22px;color:#4b4b4b;margin-bottom:14px}
.post-image{width:310px;height:176px;margin:0 auto 14px;border:2px solid var(--white);background:linear-gradient(140deg,#38b8da 0%,#4fb0d2 30%,#d81f8c 55%,#f1dc1d 75%,#c53b8e 100%)}
.post p{font-size:10.5px;line-height:18px;color:var(--ink-soft);padding:0 2px}
.post-divider{position:absolute;left:481px;top:836px;width:1px;height:150px;background:#bfc6c8}
.site-footer{position:absolute;left:0;top:1108px;width:980px;height:92px;background:var(--lime);border-top:2px solid #c5cbcd}
.copyright{position:absolute;left:123px;top:34px;font-size:11px;color:#3e4a2a}
.social{position:absolute;left:712px;top:28px;display:flex;gap:12px;font-family:"Gelasio",Georgia,serif;font-size:11px;color:#2d3a1c}
.social a{display:flex;align-items:center;gap:4px;color:#2d3a1c;text-decoration:none}
.social .dot{width:12px;height:12px;background:#3b5a8f}
</style>
</head>
<body>
<header class="site-header">
  <div class="brand"><span class="brand-mark"></span><span class="brand-name">Kestrel Hub</span></div>
  <nav class="main-nav">
    <a class="is-active" href="#">Home</a>
    <a href="#">About Us</a>
    <a href="#">Our Services</a>
    <a href="#">Contact Us</a>
  </nav>
</header>

<section class="hero">
  <p class="hero-lead">Lorem ipsum dolor sit ipsum Lorem ipsum dolor sit ipsumLorem ipsum dolor sit ip-<br>sumLorem ipsum dolor sit ipsumLorem ipsum dolor sit ipsum Lorem ipsum dolor sit<br>ipsumLorem ipsum dolor sit ipsumLorem ipsum dolor sit ipsum</p>
  <svg class="slider-arrow" style="left:87px" viewBox="0 0 34 34"><circle cx="17" cy="17" r="15" fill="none" stroke="var(--arrow)" stroke-width="2"/><path d="M20 9 L11 17 L20 25 Z" fill="var(--arrow)"/></svg>
  <div class="thumb" style="left:138px" role="img" aria-label="Colourful abstract work sample"></div>
  <div class="thumb" style="left:310px" role="img" aria-label="Colourful abstract work sample"></div>
  <div class="thumb" style="left:482px" role="img" aria-label="Colourful abstract work sample"></div>
  <div class="thumb" style="left:654px" role="img" aria-label="Colourful abstract work sample"></div>
  <svg class="slider-arrow" style="left:833px" viewBox="0 0 34 34"><circle cx="17" cy="17" r="15" fill="none" stroke="var(--arrow)" stroke-width="2"/><path d="M14 9 L23 17 L14 25 Z" fill="var(--arrow)"/></svg>
</section>

<div class="ribbon ribbon--live">OUR LIVE&nbsp;&nbsp;WORK</div>

<section class="features">
  <article class="feature">
    <h3 class="feature-title"><svg viewBox="0 0 28 28"><g fill="#3a9ad2"><circle cx="14" cy="14" r="8"/><rect x="12" y="2" width="4" height="24"/><rect x="2" y="12" width="24" height="4"/><rect x="12" y="2" width="4" height="24" transform="rotate(45 14 14)"/><rect x="12" y="2" width="4" height="24" transform="rotate(-45 14 14)"/></g><circle cx="14" cy="14" r="3.5" fill="var(--paper)"/></svg>About Us</h3>
    <p>Lorem ipsum dolor sit ipsum Lorem ipsum dolor sit ipsum Lorem ipsum dolor sit ipsum Lorem ipsum dolor sit ipsum Lorem ipsum dolor sit ipsum Lorem ipsum dolor sit ipsum Lorem ipsum dolor sit ipsum Lorem ipsum dolor sit ipsum Lorem ipsum dolor sit ipsum Lorem ipsum dolor sit ipsum Lorem ipsum dolor sit.</p>
  </article>
  <article class="feature">
    <h3 class="feature-title"><svg viewBox="0 0 28 28"><path d="M14 2a8 8 0 0 0-5 14.2V20h10v-3.8A8 8 0 0 0 14 2z" fill="#3a9ad2"/><rect x="10" y="21" width="8" height="2" fill="#3a9ad2"/><rect x="11" y="24" width="6" height="2" fill="#3a9ad2"/></svg>Our Services</h3>
    <p>Lorem ipsum dolor sit ipsum Lorem ipsum dolor sit ipsum Lorem ipsum dolor sit ipsum Lorem ipsum dolor sit ipsum Lorem ipsum dolor sit ipsum Lorem ipsum dolor sit ipsum Lorem ipsum dolor sit ipsum Lorem ipsum dolor sit ipsum Lorem ipsum dolor sit ipsum Lorem ipsum dolor sit ipsum Lorem ipsum dolor sit.</p>
  </article>
  <article class="feature">
    <h3 class="feature-title"><svg viewBox="0 0 28 28"><rect x="3" y="7" width="22" height="14" fill="none" stroke="#3a9ad2" stroke-width="1.5"/><path d="M3 7 L14 16 L25 7" fill="none" stroke="#3a9ad2" stroke-width="1.5"/></svg>Contact Us</h3>
    <p>Lorem ipsum dolor sit ipsum Lorem ipsum dolor sit ipsum Lorem ipsum dolor sit ipsum Lorem ipsum dolor sit ipsum Lorem ipsum dolor sit ipsum Lorem ipsum dolor sit ipsum Lorem ipsum dolor sit ipsum Lorem ipsum dolor sit ipsum Lorem ipsum dolor sit ipsum Lorem ipsum dolor sit ipsum Lorem ipsum dolor sit.</p>
  </article>
</section>

<div class="blog-rule"></div>
<div class="ribbon ribbon--blog">Our Blog</div>

<article class="post" style="left:128px">
  <h2>Blog Heading</h2>
  <div class="post-image" role="img" aria-label="Colourful abstract blog illustration"></div>
  <p>Lorem ipsum dolor sit ipsum Lorem ipsum dolor sit ipsum Lorem ipsum dolor sit ipsum Lorem ipsum dolor sit ipsum Lorem ipsum dolor sit ipsum Lorem ipsum dolor sit ipsum Lorem ipsum dolor sit ipsum Lorem ipsum dolor sit ipsum Lorem ipsum dolor sit ipsum Lorem ipsum dolor sit.</p>
</article>
<div class="post-divider"></div>
<article class="post" style="left:502px">
  <h2>Blog Heading</h2>
  <div class="post-image" role="img" aria-label="Colourful abstract blog illustration"></div>
  <p>Lorem ipsum dolor sit ipsum Lorem ipsum dolor sit ipsum Lorem ipsum dolor sit ipsum Lorem ipsum dolor sit ipsum Lorem ipsum dolor sit ipsum Lorem ipsum dolor sit ipsum Lorem ipsum dolor sit ipsum Lorem ipsum dolor sit ipsum Lorem ipsum dolor sit ipsum Lorem ipsum dolor sit.</p>
</article>

<footer class="site-footer">
  <p class="copyright">Copyright Text Here</p>
  <nav class="social">
    <a href="#"><span class="dot"></span>Facelane</a>
    <a href="#"><span class="dot" style="background:#3aa3dc"></span>Plovane</a>
    <a href="#"><span class="dot" style="background:#f0a02a"></span>RSS</a>
  </nav>
</footer>
</body>
</html>
```